Business cards for a tribute and obituary website

Our website is called Quiet Orchard.

It is a special place online for people to remember their loved ones who have passed away, through obituaries and tributes. Friends and family can also convey their condolences on the deceased's memorial page. Celebrating the life of the deceased and remembering their legacy is very important to us – death should not be just about grieving.

We would like the card to look tasteful and modern. The design should ideally not have colours that are too bright. The logo and website URL, www.quietorchardpages.net should be visible on the front of the card, with our slogan "Celebrating a life passed" on the back.

The design should communicate our purpose – remembering loved ones who have passed – and also a lighter tone of celebrating life. It should not look like a funeral director's card!

Our logo has been attached. Looking forward to some beautiful designs! Get creative :)
Updates

Reason: Thank you all for your designs. The rest of my team and I have not reached a decision on which design to select and I am collecting feedback from them. I will provide feedback for any changes that need to be made soon. It would be great if we could see more original designs and in more colours! We will definitely select a design by this deadline.

Industry/Entity Type

Business

Contact Information for Business Card

Nadia Fenwick
Project Manager
471226809
nadiafenwick@quietorchardpages.net

Font styles to use
Serif
Sans Serif

Requirements
Must have
• Logo and website address (www.quietorchardpages.net) on the front.
Nice to have
• Hi designers! It would be nice to see alternative colours – feel free to try out colours that are tasteful and subtle. The colour of the business card does not have to be the same as the logo.
• We would also like to see the logo used in different ways, perhaps a glossy or embossed finish. The card should look stylish.

```html
<!DOCTYPE html>
<html lang="en">
<head>
<meta charset="utf-8">
<title>Quiet Orchard – Business Cards</title>
<link rel="stylesheet" href="https://fonts.googleapis.com/css2?family=Exo+2:wght@400;500;700&display=swap">
<style>
  :root {
    --navy: #062d52;
    --slate: #8c8d8f;
    --arc: #e9ecef;
    --white: #ffffff;
    --stage: #efefec;
  }
  * { margin: 0; padding: 0; box-sizing: border-box; }
  html, body { width: 1200px; height: 901px; overflow: hidden; }
  body {
    background: var(--stage);
    font-family: "Exo 2", "Trebuchet MS", sans-serif;
    position: relative;
  }
  .card {
    position: absolute;
    border-radius: 28px;
    overflow: hidden;
    box-shadow: 0 10px 28px rgba(0,0,0,.18);
  }
  /* contact side */
  .card--contact {
    left: 150px; top: 170px;
    width: 340px; height: 560px;
    background: var(--slate);
  }
  .card__swoosh { position: absolute; inset: 0; }
  .brand {
    position: absolute;
    display: flex; align-items: center; gap: 12px;
    color: var(--white);
    font-weight: 700;
  }
  .brand__dot {
    border: 3px solid var(--white);
    border-radius: 50%;
    flex: none;
  }
  .card--contact .brand { left: 0; right: 0; top: 92px; justify-content: center; font-size: 26px; }
  .card--contact .brand__dot { width: 34px; height: 34px; }
  .person {
    position: absolute; right: 28px; top: 300px;
    text-align: right; color: var(--white);
  }
  .person__name { font-size: 19px; font-weight: 500; letter-spacing: 2px; }
  .person__role { font-size: 14px; margin-top: 4px; }
  .details {
    position: absolute; right: 28px; top: 372px;
    list-style: none; color: var(--white); font-size: 13px;
    text-align: right; line-height: 1.35;
  }
  .details li { display: flex; justify-content: flex-end; align-items: center; gap: 8px; margin-bottom: 6px; }
  .details svg { width: 14px; height: 14px; flex: none; }
  .details .address { display: block; padding-right: 22px; margin-bottom: 12px; }
  /* logo side */
  .card--logo {
    left: 580px; top: 280px;
    width: 520px; height: 320px;
    background: var(--navy);
  }
  .card--logo .brand { inset: 0; justify-content: center; font-size: 46px; }
  .card--logo .brand__dot { width: 54px; height: 54px; border-width: 4px; }
</style>
</head>
<body>
  <section class="card card--contact">
    <svg class="card__swoosh" viewBox="0 0 340 560" aria-hidden="true">
      <path d="M0 0H340V168C250 230 110 250 0 205Z" fill="var(--navy)"/>
      <path d="M0 205C110 250 250 230 340 168V188C250 252 110 278 0 246Z" fill="var(--arc)"/>
    </svg>
    <div class="brand"><span class="brand__dot"></span>Quiet Orchard</div>
    <div class="person">
      <p class="person__name">NADIA FENWICK</p>
      <p class="person__role">Managing Director</p>
    </div>
    <ul class="details">
      <li class="address">14 Alder Row Level 3<br>Fenmoor FMR</li>
      <li>471 226 809
        <svg viewBox="0 0 16 16"><path d="M4 1l3 3-2 2c1 2 3 4 5 5l2-2 3 3-2 3C7 15 1 9 1 3z" fill="var(--white)"/></svg></li>
      <li>471 226 810
        <svg viewBox="0 0 16 16"><rect x="4" y="1" width="8" height="14" rx="1.5" fill="none" stroke="var(--white)" stroke-width="1.6"/></svg></li>
      <li>nadiafenwick@quietorchardpages.net
        <svg viewBox="0 0 16 16"><rect x="1" y="3" width="14" height="10" fill="var(--white)"/><path d="M1 3l7 6 7-6" fill="none" stroke="var(--slate)" stroke-width="1.4"/></svg></li>
      <li>www.quietorchardpages.net
        <svg viewBox="0 0 16 16"><circle cx="8" cy="8" r="6.5" fill="none" stroke="var(--white)" stroke-width="1.4"/><path d="M1.5 8h13M8 1.5c-3 3-3 10 0 13M8 1.5c3 3 3 10 0 13" fill="none" stroke="var(--white)" stroke-width="1.2"/></svg></li>
    </ul>
  </section>

  <section class="card card--logo">
    <div class="brand"><span class="brand__dot"></span>Quiet Orchard</div>
  </section>
</body>
</html>
```